Real Estate Investor needs awesome business card design

I invest in real estate, focused on multi-family properties, and I need a business card to hand out to potential partners. I prefer simple, clean designs, but it needs to stand out, so I'd like there to be a bit of red in the design as well.

It should include this information:

Front
Dallin Pecksworth
Real Estate Investor
Direct phone: 502-867-3394
Email: dallinhpecksworth@quillmail.example
Headshot (Picture), I've uploaded a few, just pick the one you think looks best with your design. You can remove the background from the headshot image if it looks better.

Back
The back of the card's design should flow and be congruent with the front. On the back I want to put an inspirational quote or question. There will be different ones depending on the card, so I'll need the original file so I can edit it in the end.

For now, use “The Pessimist Sees Difficulty In Every Opportunity. The Optimist Sees The Opportunity In Every Difficulty.” -Barnaby Ellsworth

Target Market(s)

Investors

Industry/Entity Type

Real Estate

Contact Information for Business Card

Front
Dallin Pecksworth
Real Estate Investor

Back
The back of the card's design should flow and be congruent with the front. On the back I want to put an inspirational quote or question. There will be different ones depending on the card, so I'll need the original file so I can edit it in the end. I've uploaded some EXAMPLES of business cards with quotes on them. Don't copy but feel free to use them as inspiration.

The design will be printed on "ZIB sized" business cards
1039 x 697 pixels
with rounded corners

Font styles to use
Serif
Decorative
Script

Colors
ec1f27

Requirements
Must have
• Headshot, name, and other information in it.
• 1039 x 697 pixels
• Rounded corners
• Clean design that pops. I'm open to see any color background, including black.
• Headshots can be located here: https://www.filecrate.example/sh/8kd2wq7mzt31hvx/BBQTXP4ruf9LmQ0KhcvWx7b?dl=0
Nice to have
• It would be awesome if the design included a personal signature or monogram, but if not I'll get a personal logo developed later and the card redesigned if I think it needs it.
Should not have
• Cluttered design

```html
<!DOCTYPE html>
<html lang="en">
<head>
<meta charset="utf-8">
<title>Dallin Pecksworth – Business Card</title>
<link rel="stylesheet" href="https://fonts.googleapis.com/css2?family=Source+Sans+3:wght@400;600;700&display=swap">
<style>
  :root {
    --page-bg: #e8e5e1;
    --card-black: #0b0b0b;
    --card-black-soft: #1c1c1c;
    --brand-red: #ec1f27;
    --text-white: #ffffff;
    --swoosh-light: #dcdcdc;
    --card-w: 540px;
    --card-h: 362px;
  }
  * { box-sizing: border-box; margin: 0; padding: 0; }
  html, body {
    width: 1200px;
    height: 900px;
    overflow: hidden;
    background: var(--page-bg);
    font-family: "Source Sans 3", "Myriad Pro", Arial, sans-serif;
  }
  .card-sheet {
    width: 1200px;
    height: 900px;
    display: flex;
    align-items: center;
    justify-content: center;
    gap: 40px;
  }
  .card {
    position: relative;
    width: var(--card-w);
    height: var(--card-h);
    border-radius: 6px;
    overflow: hidden;
    background: radial-gradient(ellipse at 50% 30%, var(--card-black-soft) 0%, var(--card-black) 75%);
    box-shadow: 0 6px 18px rgba(0,0,0,0.25);
  }

  /* Back: quote side */
  .card--back {
    display: flex;
    flex-direction: column;
    align-items: center;
    justify-content: center;
    text-align: center;
    padding: 0 50px;
  }
  .quote-text {
    color: var(--text-white);
    font-size: 27px;
    font-weight: 400;
    line-height: 1.22;
  }
  .quote-author {
    margin-top: 10px;
    color: var(--brand-red);
    font-size: 14px;
  }

  /* Front: identity side */
  .identity {
    position: absolute;
    left: 62px;
    top: 86px;
  }
  .identity-name {
    color: var(--brand-red);
    font-size: 21px;
    font-weight: 700;
    line-height: 1.1;
  }
  .identity-title {
    color: var(--text-white);
    font-size: 15px;
    margin-top: 2px;
  }
  .contact-list {
    position: absolute;
    left: 64px;
    top: 160px;
    list-style: none;
  }
  .contact-item {
    display: flex;
    align-items: center;
    gap: 10px;
    color: var(--text-white);
    font-size: 16px;
    line-height: 1.45;
  }
  .contact-icon { width: 13px; height: 13px; flex: none; }
  .swoosh {
    position: absolute;
    inset: 0;
    width: 100%;
    height: 100%;
  }
</style>
</head>
<body>
  <main class="card-sheet">
    <section class="card card--back" aria-label="Card back">
      <p class="quote-text">“The Pessimist Sees Difficulty<br>In Every Opportunity.<br>The Optimist Sees<br>The Opportunity In<br>Every Difficulty.”</p>
      <p class="quote-author">-Barnaby Ellsworth</p>
    </section>

    <section class="card card--front" aria-label="Card front">
      <svg class="swoosh" viewBox="0 0 540 362" aria-hidden="true">
        <path fill="var(--swoosh-light)" d="M0,282 C150,330 300,292 470,205 C320,300 160,340 0,318 Z"/>
        <path fill="var(--brand-red)" stroke="#000" stroke-width="3" d="M0,322 C170,352 340,318 540,168 L540,362 L0,362 Z"/>
      </svg>

      <div class="identity">
        <h1 class="identity-name">Dallin Pecksworth</h1>
        <p class="identity-title">Real Estate Investor</p>
      </div>

      <ul class="contact-list">
        <li class="contact-item">
          <svg class="contact-icon" viewBox="0 0 16 16" aria-hidden="true">
            <path fill="var(--brand-red)" d="M1 5c0-2 2-3 7-3s7 1 7 3v1h-3V4.5H4V6H1z M3 7h10l1 7H2z"/>
            <circle cx="8" cy="10.5" r="2" fill="var(--card-black)"/>
          </svg>
          <span>502-867-3394</span>
        </li>
        <li class="contact-item">
          <svg class="contact-icon" viewBox="0 0 16 16" aria-hidden="true">
            <rect x="1" y="3" width="14" height="10" fill="var(--brand-red)"/>
            <path d="M1 3 L8 9 L15 3" fill="none" stroke="var(--card-black)" stroke-width="1.3"/>
          </svg>
          <span>dallinhpecksworth@quillmail.example</span>
        </li>
      </ul>
    </section>
  </main>
</body>
</html>
```